Pastry Trade Institute Website Homepage Revision

I need the "homepage" to the new Northfield Pastry Trade Institute to reworked. The current homepage is dull. It needs the attention of a professional graphic artist so it delivers a professionally finished feel and look. I have included the current URL for your viewing (builds.vorlimo.com/bridal-torte/cms/ ) to see where we are in the development phase. The elements on the homepage are all necessary and the colors are correct. I have also included the original Word document for the page (you can extract the RGB values and images from the doc). To be clear, I am not looking to recreate all the web pages, just the homepage. It needs to be responsive and stretched.

Target Market(s)

All bakers who sell wedding cakes in the United States

Number of Pages Required

1 page

Font styles to use
Other font styles liked:
• see the Word Document

Requirements
Must have
• It must have the elements already in the original mock up. That includes the colors and fonts.

```html
<!DOCTYPE html>
<html lang="en">
<head>
<meta charset="utf-8">
<title>Northfield Pastry Trade Institute</title>
<link href="https://fonts.googleapis.com/css2?family=Nunito+Sans:wght@300;400;600;700;800&display=swap" rel="stylesheet">
<style>
:root{
  --nav:#35241c;
  --wood-1:#6b4a38;
  --wood-2:#3f2a20;
  --copper:#d69a6a;
  --teal:#1bb5b1;
  --teal-dark:#169a97;
  --slate:#5a8b8b;
  --orange:#f7941d;
  --magenta:#b2137f;
  --footer:#560c3c;
  --headline:#d8145a;
  --ink:#333;
  --grey:#efefef;
  --white:#fff;
}
*{box-sizing:border-box;margin:0;padding:0}
html,body{width:1200px;height:3564px;overflow:hidden}
body{position:relative;font-family:"Nunito Sans",Arial,sans-serif;color:var(--ink);background:var(--white)}
.band{position:absolute;left:0;width:1200px}
.edge{position:absolute;left:0;width:1200px;display:block}

.site-nav{top:0;height:40px;background:var(--nav);display:flex;justify-content:center;align-items:center;gap:30px}
.site-nav a{color:var(--white);font-size:12px;font-weight:600;text-decoration:none;letter-spacing:.3px}
.site-nav a.active{text-decoration:underline}

.hero{top:40px;height:525px;background:linear-gradient(100deg,var(--wood-2),var(--wood-1) 45%,var(--wood-2))}
.hero-brand{position:absolute;left:0;right:0;top:210px;text-align:center;color:var(--copper);font-weight:700;font-size:64px;line-height:1.05}
.hero-arrow{position:absolute;top:252px;width:24px;height:24px}

.press{top:565px;height:148px;background:var(--white)}
.press-label{position:absolute;left:145px;top:56px;font-size:15px;font-weight:600;color:#444;line-height:1.3}
.press-badge{position:absolute;top:55px;width:48px;height:36px;background:#9c9c9c;border-radius:4px}

.video{top:713px;height:406px}
.video-media{position:absolute;left:0;top:0;width:718px;height:406px;background:linear-gradient(135deg,#6a9c9b,var(--slate) 55%,#3f6f70)}
.video-title{position:absolute;left:0;width:718px;top:148px;text-align:center;color:var(--white);font-size:46px;font-weight:800}
.video-btn{position:absolute;left:300px;top:207px;width:140px;height:38px;border:2px solid var(--white);border-radius:20px;color:var(--white);font-weight:700;font-size:15px;display:flex;align-items:center;justify-content:center;gap:6px}
.video-form{position:absolute;left:718px;top:0;width:482px;height:406px;background:var(--teal);text-align:center}
.video-form h2{margin-top:78px;color:var(--white);font-size:19px;font-weight:800;line-height:1.35;text-transform:uppercase}
.field{display:block;background:var(--white);border-radius:22px;height:42px;color:#555;font-size:13px;text-align:left;padding:12px 26px}
.video-form .field{width:292px;margin:0 auto}
.btn{display:flex;align-items:center;justify-content:center;background:var(--orange);color:var(--white);font-weight:800;font-size:15px;border-radius:22px;height:42px}
.video-form .btn{width:292px;margin:14px auto 0}

.research{top:1119px;height:461px;background:var(--teal)}
.research-lead{position:absolute;top:76px;left:0;right:0;text-align:center;color:var(--white);font-size:24px;font-weight:300;line-height:1.5}
.goal{position:absolute;top:171px;width:214px;height:214px;border-radius:50%;background:var(--white);border:6px dashed var(--teal-dark);outline:4px solid var(--white);text-align:center;padding-top:50px}
.goal svg{width:48px;height:48px}
.goal p{font-size:14px;color:var(--magenta);line-height:1.3;margin-top:10px}
.goal b{font-size:19px;font-weight:800}
.goal small{display:block;color:var(--teal-dark);font-size:12px;margin-top:6px}

.insights{top:1580px;height:510px;background:var(--white)}
.card{position:absolute;top:85px;width:297px;height:322px;background:var(--teal)}
.card-media{height:212px}
.card p{color:var(--white);font-size:14px;line-height:1.4;text-align:center;padding:0 18px;margin-top:-30px}
.card .btn{position:absolute;left:90px;bottom:-22px;width:117px;height:44px;font-size:16px}

.bio{top:2090px;height:618px;background:var(--grey);text-align:center}
.bio-photo{position:absolute;left:530px;top:80px;width:140px;height:140px;border-radius:50%;border:3px solid var(--teal);background:linear-gradient(160deg,#cfd8dc,#8ea0a8)}
.bio h2{position:absolute;top:248px;left:145px;right:145px;color:var(--headline);font-size:20px;font-weight:800;line-height:1.35}
.bio-copy{position:absolute;top:323px;left:145px;right:145px;color:var(--headline);font-size:14px;line-height:1.6}
.bio-copy p{margin-bottom:14px}
.bio-copy .cue{color:var(--orange)}
.scroll-cue{position:absolute;left:560px;top:2664px;width:80px;height:80px;border-radius:50%;background:var(--orange);border:5px solid var(--white);display:flex;align-items:center;justify-content:center;z-index:3}

.optin{top:2708px;height:381px;background:var(--teal)}
.optin h2{position:absolute;top:122px;left:145px;right:145px;text-align:center;color:var(--white);font-size:20px;font-weight:800;line-height:1.45}
.optin .field{position:absolute;top:200px;width:290px}
.optin .btn{position:absolute;top:200px;left:760px;width:293px}
.optin-note{position:absolute;top:272px;left:0;right:0;text-align:center;color:var(--white);font-size:14px}

.social{top:3089px;height:83px;background:var(--magenta);display:flex;justify-content:center;align-items:center;gap:26px}
.social span{width:22px;height:22px;border-radius:50%;background:var(--white)}

.footer{top:3172px;height:392px;background:var(--footer);color:var(--white)}
.footer-col{position:absolute;top:60px;width:220px}
.footer-col h3{font-size:19px;font-weight:700;margin-bottom:16px}
.footer-col li{list-style:none;font-size:12px;line-height:26px;color:#e8cfe0}
.post{font-size:12px;line-height:1.45;color:#e8cfe0;margin-bottom:6px}
.post-date{font-size:12px;font-weight:700;margin-bottom:18px}
.footer-rule{position:absolute;left:145px;right:145px;top:322px;border-top:1px solid rgba(255,255,255,.25)}
.copyright{position:absolute;top:343px;left:0;right:0;text-align:center;font-size:12px}
</style>
</head>
<body>

<nav class="band site-nav">
  <a class="active">HOME</a><a>HAL'S STORY</a><a>MARKETING SOLUTIONS</a><a>SALES SOLUTIONS</a><a>HIRE US</a><a>CONTACT</a><a>MEMBER LOGIN</a><a>PARTNER WITH US</a><a>BLOG</a>
</nav>

<header class="band hero" role="img" aria-label="Dark wood plank wall with the institute name mounted in copper">
  <div class="hero-brand">Northfield Pastry<br>Trade Institute</div>
  <svg class="hero-arrow" style="left:43px" viewBox="0 0 24 24"><path d="M16 3 7 12l9 9" fill="none" stroke="#fff" stroke-width="3"/></svg>
  <svg class="hero-arrow" style="left:1133px" viewBox="0 0 24 24"><path d="M8 3l9 9-9 9" fill="none" stroke="#fff" stroke-width="3"/></svg>
  <svg class="edge" style="bottom:0" height="12" viewBox="0 0 1200 12" preserveAspectRatio="none"><defs><pattern id="zzHero" width="16" height="12" patternUnits="userSpaceOnUse"><path d="M0 12 8 2 16 12Z" fill="#fff"/></pattern></defs><rect width="1200" height="12" fill="url(#zzHero)"/></svg>
</header>

<section class="band press">
  <div class="press-label">HAL BRENNER<br>AS SEEN ON</div>
  <span class="press-badge" style="left:332px"></span>
  <span class="press-badge" style="left:442px"></span>
  <span class="press-badge" style="left:556px"></span>
  <span class="press-badge" style="left:670px;border-radius:50%;width:40px;height:40px;top:53px"></span>
  <span class="press-badge" style="left:774px"></span>
  <span class="press-badge" style="left:886px"></span>
  <span class="press-badge" style="left:1005px"></span>
</section>

<section class="band video">
  <div class="video-media" role="img" aria-label="Chalkboard covered in hand-drawn notes about a wedding cake sales system">
    <div class="video-title">WATCH THIS FIRST</div>
    <div class="video-btn"><svg width="16" height="16" viewBox="0 0 16 16"><circle cx="8" cy="8" r="8" fill="#fff"/><path d="M6 4.5 11 8l-5 3.5Z" fill="#5a8b8b"/></svg>CLICK HERE</div>
  </div>
  <div class="video-form">
    <h2>How a new discovery<br>sells more wedding cakes<br>and at higher prices!</h2>
    <span class="field" style="margin-top:56px">Your First Name</span>
    <span class="field" style="margin-top:14px">Your Email</span>
    <span class="btn">WATCH NOW!</span>
  </div>
</section>

<section class="band research">
  <p class="research-lead">Our research is not just a game changer. It is the game changer.<br>We're rewriting the book for selling wedding cakes</p>

  <div class="goal" style="left:147px">
    <svg viewBox="0 0 48 48"><path d="M6 22 26 4h16v16L24 40Z" fill="#169a97"/><circle cx="35" cy="12" r="3" fill="#fff"/></svg>
    <p>I'm <b>New</b> to Selling<br>Wedding Cakes...<small>Click Here</small></p>
  </div>
  <div class="goal" style="left:378px">
    <svg viewBox="0 0 48 48"><path d="M2 8h8l6 22h24l5-16H13" fill="none" stroke="#169a97" stroke-width="4"/><circle cx="19" cy="38" r="3.5" fill="#169a97"/><circle cx="36" cy="38" r="3.5" fill="#169a97"/></svg>
    <p>I Want to <b>Maintain</b><br>My Sales...<small>Click Here</small></p>
  </div>
  <div class="goal" style="left:606px">
    <svg viewBox="0 0 48 48"><rect x="6" y="32" width="6" height="10" fill="#169a97"/><rect x="16" y="25" width="6" height="17" fill="#169a97"/><rect x="26" y="18" width="6" height="24" fill="#169a97"/><rect x="36" y="10" width="6" height="32" fill="#169a97"/><path d="M4 26 40 4" stroke="#169a97" stroke-width="3"/></svg>
    <p>I'm Eager to <b>Boost</b> My<br>Sales and Profits...<small>Click Here</small></p>
  </div>
  <div class="goal" style="left:836px">
    <svg viewBox="0 0 48 48"><rect x="10" y="4" width="4" height="40" fill="#169a97"/><path d="M14 6h26l-6 9 6 9H14Z" fill="#169a97"/></svg>
    <p>I'm Ready to <b>Dominate</b><br>My Market Area...<small>Click Here</small></p>
  </div>

  <svg class="edge" style="bottom:0" height="12" viewBox="0 0 1200 12" preserveAspectRatio="none"><defs><pattern id="zzResearch" width="16" height="12" patternUnits="userSpaceOnUse"><path d="M0 12 8 2 16 12Z" fill="#fff"/></pattern></defs><rect width="1200" height="12" fill="url(#zzResearch)"/></svg>
</section>

<section class="band insights">
  <article class="card" style="left:145px">
    <div class="card-media" role="img" aria-label="Three bakers in white chef uniforms" style="background:linear-gradient(180deg,#3c6f78,#1bb5b1)"></div>
    <p>Become the "Bride's First Choice." You'll have an atmosphere so special, brides won't think of using anyone but you!</p>
    <span class="btn">MORE</span>
  </article>
  <article class="card" style="left:451px">
    <div class="card-media" role="img" aria-label="Puzzled woman beside a large question mark" style="background:linear-gradient(180deg,#2f6b70,#1bb5b1)"></div>
    <p>Peek at a very effective psychological sales riddle called "The Doubt Divide."</p>
    <span class="btn">MORE</span>
  </article>
  <article class="card" style="left:758px">
    <div class="card-media" role="img" aria-label="Split portrait of a woman showing two expressions" style="background:linear-gradient(180deg,#8fa7a8,#1bb5b1)"></div>
    <p>Discover a sales growth secret that reveals the "Two Sides of Your Cake Studio."</p>
    <span class="btn">MORE</span>
  </article>
</section>

<section class="band bio">
  <div class="bio-photo" role="img" aria-label="Portrait of the institute founder"></div>
  <h2>Use Cutting-edge Methods Proven to Get MORE Leads, Convince MORE Brides to Choose You,<br>Get HIGHER Prices and DOMINATE Your Competition</h2>
  <div class="bio-copy">
    <p>Our breakthrough marketing and sales methods are possible due to the long-term studies we've conducted with 150,000 brides over the past 12 years.</p>
    <p>From the findings, we have developed new and revolutionary marketing strategies, sales tools, and a complete transformational wedding cake sales system.</p>
    <p>But, don't take my word for it...let me "prove" the value and impact they will have on your wedding cake business.</p>
    <p class="cue">Enter Your Name and Email Address Below.</p>
    <p>Each month you'll receive our "Monthly Cake Studio Research Letter." It's normally available for a $397 subscription fee. You'll receive the first year... absolutely FREE.</p>
  </div>
</section>

<div class="scroll-cue"><svg width="30" height="36" viewBox="0 0 30 36"><path d="M15 2v28M4 20l11 12 11-12" fill="none" stroke="#fff" stroke-width="5"/></svg></div>

<section class="band optin">
  <svg class="edge" style="top:0" height="12" viewBox="0 0 1200 12" preserveAspectRatio="none"><defs><pattern id="zzOptin" width="16" height="12" patternUnits="userSpaceOnUse"><path d="M0 0 8 10 16 0Z" fill="#efefef"/></pattern></defs><rect width="1200" height="12" fill="url(#zzOptin)"/></svg>
  <h2>Join our "Research Letter" for FREE. You'll receive the latest research secrets while learning how to use psychology for gaining a decisive advantage to market and sell your wedding cakes.</h2>
  <span class="field" style="left:145px">Your First Name</span>
  <span class="field" style="left:453px">Your Email</span>
  <span class="btn">WATCH NOW!</span>
  <p class="optin-note">We dislike spam as much as you do. Therefore, we'll never sell, rent, or give away your email address.</p>
</section>

<section class="band social">
  <svg class="edge" style="top:0" height="12" viewBox="0 0 1200 12" preserveAspectRatio="none"><defs><pattern id="zzSocial" width="16" height="12" patternUnits="userSpaceOnUse"><path d="M0 0 8 10 16 0Z" fill="#1bb5b1"/></pattern></defs><rect width="1200" height="12" fill="url(#zzSocial)"/></svg>
  <span></span><span></span><span></span><span></span><span></span>
</section>

<footer class="band footer">
  <div class="footer-col" style="left:145px">
    <h3>Marketing Solutions</h3>
    <ul><li>Core Pricing Foundations Course</li><li>Individual Marketing Videos</li><li>Bundled Marketing Videos</li><li>Trusted Studio Baker</li><li>Advertise For Free</li><li>Analyze Your Marketing</li><li>Buyer Priorities Training</li></ul>
  </div>
  <div class="footer-col" style="left:378px">
    <h3>Sales Solutions</h3>
    <ul><li>Individual Sales Tools</li><li>Bundles Sales Presentations</li><li>Monthly Research Notes</li><li>Write a Wedding Cake Book</li><li>Analyze Your Sales System</li></ul>
  </div>
  <div class="footer-col" style="left:613px">
    <h3>Hire Us</h3>
    <ul><li>Coaching</li><li>Consulting</li><li>Speaking</li><li>3-Day Workshops</li></ul>
    <h3 style="margin-top:20px">Partner With Us</h3>
    <ul><li>Spread the Word</li></ul>
  </div>
  <div class="footer-col" style="left:846px;width:210px">
    <h3>Recent Blog Posts</h3>
    <p class="post">Fusce eget neque elit. Sed augue orci, elementum in magna congue, tincidunt vulputate erat.</p>
    <p class="post-date">7 Jan, 2019</p>
    <p class="post">Aliquam consectetur orci molestie dictum molestie. Proin eget congue nulla, vel tempor.</p>
    <p class="post-date">7 Jan, 2019</p>
  </div>
  <div class="footer-rule"></div>
  <p class="copyright">Copyright © 2019 Northfield Pastry Trade Institute. All rights reserved.</p>
</footer>

</body>
</html>
```